Color Revisions on Page File

We need the colors in the attached "New Profile View" file revised to match and flow seamlessly with our new Home Page (attached file "New Home").
Source file for Profile View attached as well.
We do not need any page elements re-positioned. This is all about optimizing colors to ensure a nice modern look and consistent navigation.
You only need to submit top half of the page until winner is selected. This will prevent unnecessary work on your end. Upon selection, you can complete the makeover.
Please submit your best design at earliest possible, as this is a rush project. Thanks greatly!
Please focus on the lighter colors with only dark attributes. This new look should be fresh and crisp - with an appearance comparable to best-in-class solutions. Thanks.
PLEASE NOTE: I have just uploaded another file called "Sample5". Please use similar color scheme to this in your design. Thank you!

```html
<!DOCTYPE html>
<html lang="en">
<head>
<meta charset="utf-8">
<title>Reachgauge – Profile View</title>
<link rel="stylesheet" href="https://fonts.googleapis.com/css2?family=Arimo:wght@400;700&family=Open+Sans:wght@300;400;600&display=swap">
<style>
:root{
  --ink:#1d1d1d;
  --muted:#555;
  --header-grey:#e9e7e3;
  --sky:#2f8be0;
  --sky-deep:#1a6fc8;
  --sky-pale:#d7ecfb;
  --chirp:#5bd3f7;
  --chirp-deep:#39b6e6;
  --circle:#1275c0;
  --circle-deep:#0d5fa1;
  --link:#0d78b8;
  --lime:#8fcf1a;
  --lime-deep:#6fb30d;
  --sun:#f6c21a;
  --red:#e0262b;
  --orange:#f08a1c;
  --green:#18a83b;
  --tile:#e8e6e2;
  --panel-light:#e4f5fd;
  --facebar:#3a5eb0;
  --white:#fff;
}
*{box-sizing:border-box;margin:0;padding:0}
html,body{width:1167px;height:1200px;overflow:hidden}
body{position:relative;font-family:"Arimo",Arial,sans-serif;color:var(--ink);font-size:11px;
  background:linear-gradient(180deg,#2f8be0 123px,#8cc6f0 330px,#cfe7f8 700px,#9fd0f3 1200px)}
.abs{position:absolute}
.topbar{left:0;top:0;width:1167px;height:25px;background:#050505}
.topline{left:0;top:25px;width:1167px;height:5px;background:var(--sky-deep)}
.header{left:0;top:30px;width:1167px;height:93px;background:var(--header-grey)}
.brand{left:146px;top:54px;font-size:36px;font-weight:700;color:var(--sky-deep);letter-spacing:-1px}
.tagline{left:146px;top:97px;font-size:14px;color:#6a6a6a;letter-spacing:.5px}
.social{left:910px;top:41px;display:flex;gap:6px}
.social span{width:20px;height:20px;border-radius:50%;background:#c9c7c3;border:1px solid #b0aeaa}
.gear{left:972px;top:78px}
.bio-label{left:146px;top:144px;color:var(--white);font-weight:700;font-size:11px}
.bio-sub{left:146px;top:162px;color:#9fd2ff;font-style:italic;font-size:11px}
.bio-div{left:275px;top:135px;width:1px;height:44px;background:#8fc4f0}
.bio-text{left:290px;top:144px;width:420px;color:var(--white);font-size:11px;line-height:16px}
.progress{left:811px;top:141px;width:195px;height:12px;background:#1a5fa8;border:1px solid #6aaae8}
.progress i{display:block;height:100%;width:70%;background:linear-gradient(90deg,#e83a2a,#f4a21f 60%,#e7c84a)}
.progress-label{left:811px;top:163px;color:var(--white);font-size:11px}

.card{left:130px;top:190px;width:893px;height:459px;background:var(--white);border-radius:6px}
.avatar{left:148px;top:208px;width:87px;height:86px;background:linear-gradient(#bdbdbd,#8f8f8f);border:3px solid #ddd}
.name{left:246px;top:205px;font-size:15px;color:var(--link);line-height:18px}
.stars{left:246px;top:245px;display:flex;gap:1px}
.info{left:146px;font-size:11px}
.box{left:146px;width:214px;background:var(--panel-light);padding:10px 12px;font-size:11px;line-height:16.5px}
.box h4{font-size:11px;font-weight:700;margin-bottom:5px}
.plain{left:146px;width:214px;padding:0 12px;font-size:11px;line-height:16.5px}
.plain h4{font-size:11px;margin-bottom:6px}
.row{display:flex}
.row b{font-weight:400;width:74px}
.lang{display:grid;grid-template-columns:74px 80px;row-gap:3px;padding-left:2px}
.lang span::before{content:"•";color:#999;margin-right:7px}
.btn{height:23px;border-radius:2px;color:var(--white);font-weight:700;font-size:11px;display:flex;align-items:center;gap:10px;padding-left:10px}

.net{left:372px;width:360px}
.net-chirp{top:208px;height:125px;background:var(--chirp)}
.net-circle{top:337px;height:142px;background:var(--circle)}
.net-link{top:483px;height:106px;background:var(--link)}
.net-name{position:absolute;left:10px;font-weight:700;color:var(--white);font-size:13px}
.count{position:absolute;left:0;width:76px;text-align:center;font-size:11px;line-height:15px;font-weight:700}
.tiny-btn{position:absolute;left:11px;width:53px;height:20px;border-radius:2px;background:linear-gradient(#7fd6f6,#3fb0e2);border:1px solid #fff;color:var(--white);font-size:11px;font-weight:700;text-align:center;line-height:18px}
.lbl{position:absolute;left:79px;font-size:11px}
.chip{position:absolute;height:27px;background:linear-gradient(#fff,#ececec);border-radius:2px;font-weight:700;font-size:13px;line-height:27px;text-align:center}
.wide-chip{position:absolute;left:79px;width:164px;height:29px;background:linear-gradient(#fff,#e8e8e8);border-radius:2px;color:var(--red);font-size:11px;font-weight:700;line-height:29px;padding-left:10px}
.ring{position:absolute}
.rank{position:absolute;left:256px;font-size:11px}
.connect{position:absolute;left:79px;top:50px;width:256px;height:33px;background:linear-gradient(#fff,#dedede);border-radius:3px;color:var(--red);font-weight:700;font-size:15px;text-align:center;line-height:33px}

.strength{left:732px;top:208px;width:272px;height:381px;background:linear-gradient(160deg,#9ad61f,#7cc312)}
.strength .kicker{position:absolute;left:19px;top:9px;color:#fff6a8;font-size:15px}
.strength .big{position:absolute;left:17px;top:22px;font-family:"Open Sans",sans-serif;font-weight:300;font-size:46px;color:#fff475;letter-spacing:3px}
.strength .factor{position:absolute;right:18px;top:68px;color:var(--white);font-family:"Open Sans",sans-serif;font-size:15px}
.scores{position:absolute;left:19px;top:130px;color:var(--white);font-weight:700;font-size:15px;line-height:24px}
.srank{position:absolute;right:20px;top:243px;color:var(--white);font-family:"Open Sans",sans-serif;font-size:15px}
.sdesc{position:absolute;left:19px;top:270px;width:240px;color:var(--white);font-size:11px;line-height:16.5px}
.source{position:absolute;left:111px;top:359px;color:var(--white);font-size:11px}
.source-icon{position:absolute;right:0;bottom:0;width:34px;height:34px;background:var(--lime-deep)}
.actions{left:828px;top:602px;display:flex;gap:2px}
.actions span{width:34px;height:32px;background:#555}

.section{left:130px;width:893px;background:var(--white);border-radius:6px 6px 0 0}
.sec-head{height:43px;display:flex;align-items:center;padding-left:73px;color:var(--white);font-size:22px;font-weight:700;position:relative;border-radius:6px 6px 0 0}
.sec-head .ico{position:absolute;left:30px;top:8px;width:26px;height:26px;border-radius:50%;background:rgba(255,255,255,.9)}
.sec-head .notch{position:absolute;left:55px;bottom:-12px;width:0;height:0;border-left:14px solid transparent;border-right:14px solid transparent}
.sec-head .toggle{position:absolute;right:16px;top:12px;width:20px;height:20px;border-radius:50%;border:1px solid rgba(255,255,255,.9)}
.sec-head .toggle::after{content:"";position:absolute;left:5px;top:9px;width:8px;height:1px;background:var(--white)}
.col-title{position:absolute;font-size:15px}
.stat{position:absolute;height:33px;background:var(--tile);border-radius:2px;display:flex;align-items:center;font-size:11px}
.stat .si{width:20px;height:14px;margin:0 11px 0 10px;border-radius:2px}
.stat .v{margin-left:auto;margin-right:14px;font-size:15px;font-weight:700;color:#333}
.fv{position:absolute;top:762px;height:32px;width:76px;border:1px solid #ddd;border-radius:2px;font-size:22px;text-align:center;line-height:32px;background:#fafafa}
.fv sup{font-size:12px}
.legend{position:absolute;left:747px;width:255px;font-size:11px;line-height:14px;padding-left:16px}
.legend i{position:absolute;left:0;top:3px;width:7px;height:7px}
.list{position:absolute;top:996px;height:94px;width:250px;background:#f2f1ef;border-radius:2px;padding:2px 0 0 14px;font-size:11px}
.list div{width:210px;height:29px;line-height:29px;border-bottom:1px solid #dcdcdc}
.list div:last-child{border:0}
.list .bar{position:absolute;right:8px;top:6px;width:8px;height:82px;background:#fff;border-radius:4px}
.list .bar::after{content:"";position:absolute;left:0;top:0;width:8px;height:32px;border-radius:4px;background:#555}
</style>
</head>
<body>
<div class="abs topbar"></div>
<div class="abs topline"></div>
<div class="abs header"></div>
<div class="abs brand">Reachgauge</div>
<div class="abs tagline">The Source for Networking Superstars</div>
<div class="abs social"><span></span><span></span><span></span><span></span></div>
<svg class="abs gear" width="38" height="38" viewBox="0 0 38 38" aria-hidden="true">
  <g fill="#555"><circle cx="19" cy="19" r="13"/>
  <rect x="16" y="1" width="6" height="36" rx="1"/><rect x="1" y="16" width="36" height="6" rx="1"/>
  <rect x="16" y="1" width="6" height="36" rx="1" transform="rotate(45 19 19)"/><rect x="16" y="1" width="6" height="36" rx="1" transform="rotate(-45 19 19)"/></g>
  <circle cx="19" cy="19" r="8" fill="var(--header-grey)"/><circle cx="19" cy="19" r="4" fill="#555"/>
</svg>

<div class="abs bio-label">BIO SUMMARY</div>
<div class="abs bio-sub">in 140 characters or less</div>
<div class="abs bio-div"></div>
<div class="abs bio-text">An absolute one stop shop for identifying, analyzing and verifying anyone's social networking abilities and value.</div>
<div class="abs progress"><i></i></div>
<div class="abs progress-label">PROFILE IS 70% COMPLETE</div>

<div class="abs card"></div>
<div class="abs avatar" role="img" aria-label="Profile photo placeholder"></div>
<div class="abs name">Meera Anand<br>Kulkarni</div>
<div class="abs stars">
  <svg width="64" height="12" viewBox="0 0 64 12" aria-hidden="true">
    <g><polygon points="6,0 7.6,4.2 12,4.4 8.6,7.2 9.8,11.6 6,9 2.2,11.6 3.4,7.2 0,4.4 4.4,4.2" fill="var(--red)"/>
    <polygon transform="translate(13 0)" points="6,0 7.6,4.2 12,4.4 8.6,7.2 9.8,11.6 6,9 2.2,11.6 3.4,7.2 0,4.4 4.4,4.2" fill="#bbb"/>
    <polygon transform="translate(26 0)" points="6,0 7.6,4.2 12,4.4 8.6,7.2 9.8,11.6 6,9 2.2,11.6 3.4,7.2 0,4.4 4.4,4.2" fill="#bbb"/>
    <polygon transform="translate(39 0)" points="6,0 7.6,4.2 12,4.4 8.6,7.2 9.8,11.6 6,9 2.2,11.6 3.4,7.2 0,4.4 4.4,4.2" fill="#bbb"/>
    <polygon transform="translate(52 0)" points="6,0 7.6,4.2 12,4.4 8.6,7.2 9.8,11.6 6,9 2.2,11.6 3.4,7.2 0,4.4 4.4,4.2" fill="#bbb"/></g>
  </svg>
</div>
<div class="abs info" style="top:305px">Location: New York</div>
<div class="abs info" style="top:322px">Position: Full time, Part Time &amp; Promotional</div>
<div class="abs box" style="top:343px;height:87px">
  <h4>Industries, Topics or Focus:</h4>
  <div class="row"><b style="width:43px">Major -</b>Internet/Media</div>
  <div class="row"><b style="width:43px">Minor -</b>Art/Photography</div>
  <div class="row"><b style="width:43px">Minor -</b>Design/Printing/Publishing</div>
</div>
<div class="abs plain" style="top:440px">
  <h4>Promotion Experience:</h4>
  <div class="row"><b>Sales -</b>2 Years</div>
  <div class="row"><b>Marketing -</b>0 Years</div>
  <div class="row"><b>Advertising -</b>8 Years</div>
</div>
<div class="abs box" style="top:518px;height:71px">
  <h4>Language Known:</h4>
  <div class="lang"><span>English</span><span>Marathi</span><span>Hindi</span><span>French</span></div>
</div>
<div class="abs btn" style="left:146px;top:606px;width:99px;background:var(--sky-deep)">
  <svg width="14" height="14" viewBox="0 0 14 14" aria-hidden="true"><g fill="none" stroke="#fff" stroke-width="2"><rect x="1" y="6" width="7" height="4" rx="2" transform="rotate(-45 4.5 8)"/><rect x="6" y="4" width="7" height="4" rx="2" transform="rotate(-45 9.5 6)"/></g></svg>Links</div>
<div class="abs btn" style="left:261px;top:606px;width:99px;background:#555">
  <svg width="12" height="14" viewBox="0 0 12 14" aria-hidden="true"><g fill="none" stroke="#fff" stroke-width="1.2"><path d="M1 1h7l3 3v9H1z"/><path d="M3 6h6M3 8h6M3 10h6"/></g></svg>Resume</div>

<!-- Chirpline summary -->
<div class="abs net net-chirp">
  <div class="net-name" style="top:14px">Chirpline</div>
  <div class="count" style="top:85px">1,900,432<br><span style="font-weight:400">Followers</span></div>
  <div class="tiny-btn" style="top:101px">Follow</div>
  <div class="lbl" style="top:16px">Account Since:&nbsp; 12/15/2009</div>
  <div class="lbl" style="top:44px">Follower Validation</div>
  <div class="chip" style="left:79px;top:67px;width:54px;color:var(--red)">0 <small>%</small></div>
  <div class="chip" style="left:135px;top:67px;width:54px;color:var(--orange)">25 <small>%</small></div>
  <div class="chip" style="left:191px;top:67px;width:54px;color:var(--green)">75 <small>%</small></div>
  <svg class="ring" style="left:264px;top:13px" width="80" height="80" viewBox="0 0 80 80" aria-hidden="true">
    <circle cx="40" cy="40" r="37" fill="#fff"/>
    <circle cx="40" cy="40" r="30" fill="none" stroke="#c9eef9" stroke-width="10"/>
    <circle cx="40" cy="40" r="30" fill="none" stroke="#27b0c9" stroke-width="10" stroke-dasharray="60.3 188.5" transform="rotate(-90 40 40)"/>
    <circle cx="40" cy="40" r="23" fill="#1c79c8"/>
    <text x="40" y="47" text-anchor="middle" fill="#fff" font-family="Arimo,sans-serif" font-size="20">32<tspan font-size="9" dy="-9">%</tspan></text>
  </svg>
  <div class="rank" style="top:105px;left:282px">ranking: 32 / 100%</div>
</div>

<!-- Circlebook summary -->
<div class="abs net net-circle">
  <div class="net-name" style="top:14px">Circlebook</div>
  <div class="count" style="top:81px;color:#fff">1,230<br><span style="font-weight:400">Friends</span></div>
  <div class="tiny-btn" style="top:110px;background:linear-gradient(#2a8cdb,#0d5fa1)">Friend</div>
  <div class="lbl" style="top:30px;color:#fff">Account Since:&nbsp; 2/19/2010</div>
  <div class="wide-chip" style="top:49px">Top Country:&nbsp; US (88%)</div>
  <div class="wide-chip" style="top:87px">Top State:&nbsp; TX (73%)</div>
  <svg class="ring" style="left:264px;top:14px" width="80" height="80" viewBox="0 0 80 80" aria-hidden="true">
    <circle cx="40" cy="40" r="37" fill="#fff"/>
    <circle cx="40" cy="40" r="30" fill="none" stroke="#c9eef9" stroke-width="10"/>
    <circle cx="40" cy="40" r="30" fill="none" stroke="#27b0c9" stroke-width="10" stroke-dasharray="94.2 188.5" transform="rotate(-90 40 40)"/>
    <circle cx="40" cy="40" r="23" fill="#1c79c8"/>
    <text x="40" y="47" text-anchor="middle" fill="#fff" font-family="Arimo,sans-serif" font-size="20">50<tspan font-size="9" dy="-9">%</tspan></text>
  </svg>
  <div class="rank" style="top:113px;left:257px;color:#fff">ranking: 50 / 100%</div>
</div>

<!-- Linkwork summary -->
<div class="abs net net-link">
  <div class="net-name" style="top:38px">Linkwork</div>
  <div class="lbl" style="top:32px;color:#fff">Login to establish your Networks here.</div>
  <div class="connect">CONNECT NOW</div>
</div>

<div class="abs strength">
  <div class="kicker">Reachgauge</div>
  <div class="big">STRENGTH</div>
  <div class="factor">Factor</div>
  <div class="scores">B2B:&nbsp; 41.7<br>B2C:&nbsp; 46.2<br>AVG:&nbsp; 43.9</div>
  <svg style="position:absolute;left:112px;top:89px" width="142" height="142" viewBox="0 0 142 142" aria-hidden="true">
    <circle cx="71" cy="71" r="69" fill="#f9e65a"/>
    <circle cx="71" cy="71" r="62" fill="#fff"/>
    <circle cx="71" cy="71" r="55" fill="none" stroke="#f4ecd0" stroke-width="9"/>
    <circle cx="71" cy="71" r="55" fill="none" stroke="#3d7fd0" stroke-width="9" stroke-dasharray="76 345.6" transform="rotate(-90 71 71)"/>
    <circle cx="71" cy="71" r="48" fill="var(--sun)"/>
    <text x="68" y="86" text-anchor="middle" fill="#fff" font-family="Open Sans,sans-serif" font-size="42">22<tspan font-size="14" dy="-22">%</tspan></text>
  </svg>
  <div class="srank">ranking: 22 / 100%</div>
  <div class="sdesc">Proprietary Scoring based on the number of network contacts within this profile and the level of impact each social channel has in relation to proven inbound marketing results (B2C).</div>
  <div class="source">VIEW SOURCE STUDY</div>
  <div class="source-icon"><svg width="34" height="34" viewBox="0 0 34 34" aria-hidden="true"><g fill="none" stroke="#fff" stroke-width="1.2"><path d="M11 9h9l4 4v13H11z"/><path d="M14 16h7M14 19h7M14 22h7"/></g></svg></div>
</div>

<div class="abs actions">
  <span><svg width="34" height="32" viewBox="0 0 34 32" aria-hidden="true"><path d="M17 25l-8-8a5 5 0 0 1 8-6 5 5 0 0 1 8 6z" fill="#fff"/></svg></span>
  <span><svg width="34" height="32" viewBox="0 0 34 32" aria-hidden="true"><g fill="none" stroke="#fff" stroke-width="1.6"><rect x="7" y="9" width="20" height="14"/><path d="M7 9l10 8 10-8"/></g></svg></span>
  <span><svg width="34" height="32" viewBox="0 0 34 32" aria-hidden="true"><g fill="none" stroke="#fff" stroke-width="2"><path d="M17 10L10 23M17 10l7 13"/></g><g fill="#fff"><circle cx="17" cy="9" r="3"/><circle cx="10" cy="23" r="3"/><circle cx="24" cy="23" r="3"/></g></svg></span>
  <span><svg width="34" height="32" viewBox="0 0 34 32" aria-hidden="true"><g fill="#fff"><rect x="12" y="7" width="10" height="5"/><rect x="7" y="12" width="20" height="9" rx="2"/><rect x="12" y="19" width="10" height="6" stroke="#555"/></g></svg></span>
  <span><svg width="34" height="32" viewBox="0 0 34 32" aria-hidden="true"><g fill="none" stroke="#fff" stroke-width="2"><path d="M17 7v12M12 14l5 5 5-5M8 18v6h18v-6"/></g></svg></span>
</div>

<!-- Chirpline detail section -->
<div class="abs section" style="top:668px;height:443px;border-radius:6px">
  <div class="sec-head" style="background:var(--chirp)"><span class="ico"></span>Chirpline<span class="notch" style="border-top:12px solid var(--chirp)"></span><span class="toggle"></span></div>
</div>
<div class="col-title" style="left:167px;top:736px">Influence by @RGsample</div>
<div class="col-title" style="left:457px;top:737px">Outreach by @RGsample</div>
<div class="col-title" style="left:751px;top:737px">Follower Validation</div>

<div class="stat" style="left:164px;top:761px;width:246px"><i class="si" style="background:var(--red)"></i>Followers<span class="v">9,641</span></div>
<div class="stat" style="left:164px;top:797px;width:246px"><i class="si" style="background:var(--red)"></i><span style="line-height:13px">@ RGsample tweets,<br>RTed</span><span class="v">3,107</span></div>
<div class="stat" style="left:164px;top:833px;width:246px"><i class="si" style="background:var(--red)"></i>Replies received<span class="v">2,593</span></div>
<div class="stat" style="left:164px;top:869px;width:246px"><i class="si" style="background:var(--red)"></i>Listed<span class="v">14</span></div>
<div class="stat" style="left:164px;top:906px;width:246px"><i class="si" style="background:var(--red)"></i>RGsample mentioned<span class="v">6,214</span></div>

<div class="stat" style="left:449px;top:761px;width:254px"><i class="si" style="background:var(--chirp-deep)"></i>Following<span class="v">6,265</span></div>
<div class="stat" style="left:449px;top:797px;width:254px"><i class="si" style="background:var(--chirp-deep)"></i>RTs by @RGsample<span class="v">1,476</span></div>
<div class="stat" style="left:449px;top:833px;width:254px"><i class="si" style="background:var(--chirp-deep)"></i>@Replies sent<span class="v">1,203</span></div>
<div class="stat" style="left:449px;top:869px;width:254px"><i class="si" style="background:var(--chirp-deep)"></i>Links posted<span class="v">2,914</span></div>
<div class="stat" style="left:449px;top:906px;width:254px"><i class="si" style="background:var(--chirp-deep)"></i>Names mentioned<span class="v">6,214</span></div>

<div class="fv" style="left:745px;color:var(--red)">0<sup>%</sup></div>
<div class="fv" style="left:828px;color:var(--orange)">25<sup>%</sup></div>
<div class="fv" style="left:910px;color:var(--green)">75<sup>%</sup></div>
<div class="legend" style="top:804px"><i style="background:var(--red)"></i>Lorem ipsum dolor sit amet, consectetur adipiscing elit. Nam ullamcorper feugiat neque.</div>
<div class="legend" style="top:839px"><i style="background:var(--orange)"></i>Lorem ipsum dolor sit amet, consectetur adipiscing elit. Nam ullamcorper feugiat neque.</div>
<div class="legend" style="top:872px"><i style="background:var(--green)"></i>Lorem ipsum dolor sit amet, consectetur adipiscing elit. Nam ullamcorper feugiat neque.</div>
<div class="abs" style="left:853px;top:916px;font-size:11px">As defined by:</div>
<div class="abs" style="left:932px;top:908px;width:56px;height:28px;border-radius:3px;background:#4cc3e8"></div>

<div class="col-title" style="left:167px;top:970px">Most Mentioned</div>
<div class="col-title" style="left:457px;top:971px">Most Used</div>
<div class="col-title" style="left:751px;top:971px">Most posted links</div>
<div class="list" style="left:164px"><div>Lorem ipsum dolor sit amet</div><div>Lorem ipsum dolor sit ametsasas assa</div><div>Lorem ipsum dolor sit ametdsdsdsds</div><span class="bar"></span></div>
<div class="list" style="left:449px;width:254px"><div>Lorem ipsum dolor sit amet</div><div>Lorem ipsum dolor sit ametsasas assa</div><div>Lorem ipsum dolor sit ametdsdsdsds</div><span class="bar"></span></div>
<div class="list" style="left:744px;width:247px"><div>Lorem ipsum dolor sit amet</div><div>Lorem ipsum dolor sit ametsasas assa</div><div>Lorem ipsum dolor sit ametdsdsdsds</div><span class="bar"></span></div>

<!-- Circlebook detail section -->
<div class="abs section" style="top:1131px;height:69px">
  <div class="sec-head" style="background:var(--facebar)"><span class="ico"></span>Circlebook<span class="notch" style="border-top:12px solid var(--facebar)"></span><span class="toggle"></span></div>
</div>
</body>
</html>
```